"Nail Care" Postcard

Hello,

We are looking to redesign our current post card. The target audience of this post card age is 50+. We will be mailing these postcards through Harbor Press.
The goal of the message is to remind them that it is time to get their (toe) nail care done.

Attached is our previous postcard.
Post card size: 4.2” x 5.5”
Backside of the postcards needs space for the mailing address and postage.
Our address and logo need to be present.
The message of the back of the postcard needs to be present as well.
Examples of stock images must come with the example.
Files preferred to be in TIFF or .ai

Thank you,
Marcus T.

```html
<!DOCTYPE html>
<html lang="en">
<head>
<meta charset="utf-8">
<title>Nail Care Reminder Postcard</title>
<link href="https://fonts.googleapis.com/css2?family=Roboto+Slab:wght@700&family=Poppins:wght@400;600;700&family=Fira+Sans:wght@400;600&family=Noto+Serif&display=swap" rel="stylesheet">
<style>
  :root{
    --stage:#8f8f8f;
    --paper:#ffffff;
    --orange:#f4875a;
    --teal:#5bbfa6;
    --teal-deep:#2f9e84;
    --ink:#1d1d1d;
    --mail-grey:#e0e0e0;
  }
  *{margin:0;padding:0;box-sizing:border-box}
  html,body{width:1040px;height:1200px;overflow:hidden;background:var(--stage)}
  .card{position:absolute;left:236px;width:577px;height:440px;background:var(--paper);box-shadow:0 2px 6px rgba(0,0,0,.35);overflow:hidden}
  .card--front{top:131px}
  .card--back{top:645px;background:var(--mail-grey)}
  .layer{position:absolute;left:0;top:0}

  /* front */
  .brand{position:absolute;font-family:'Fira Sans',sans-serif;font-weight:600;color:var(--orange);text-align:right;line-height:1}
  .brand--front{right:23px;top:37px;font-size:17.5px}
  .brand .brand-site{font-size:7px;margin-top:3px;display:block}
  .brand-mark{position:absolute;border-radius:50%;background:var(--teal)}
  .brand-mark--front{left:385px;top:35px;width:36px;height:36px}
  .tagline{position:absolute;left:22px;top:337px;font-family:'Poppins',sans-serif;font-size:20px;line-height:26px;color:var(--ink)}
  .headline{position:absolute;left:22px;top:358px;font-family:'Poppins',sans-serif;font-weight:700;font-size:30px;line-height:27px;letter-spacing:-.3px}
  .headline .hl-orange{color:var(--orange);display:block}
  .headline .hl-teal{color:var(--teal);display:block}
  .front-phone{position:absolute;right:32px;top:334px;font-family:'Poppins',sans-serif;font-weight:600;font-size:28px;line-height:36px;color:var(--orange)}
  .front-site{position:absolute;right:32px;top:365px;font-family:'Poppins',sans-serif;font-weight:600;font-size:14.5px;line-height:18px;color:var(--teal)}
  .social-dot{position:absolute;top:391px;width:29px;height:29px;border-radius:50%;border:2px solid #fff}
  .social-dot--one{left:419px;background:var(--teal-deep)}
  .social-dot--two{left:451px;background:var(--orange)}

  /* back */
  .brand--back{right:403px;top:25px;font-size:13.5px}
  .brand--back .brand-site{font-size:6px;margin-top:2px}
  .brand-mark--back{left:31px;top:23px;width:24px;height:24px}
  .return-address{position:absolute;left:31px;top:66px;font-family:'Noto Serif',serif;font-size:11.5px;line-height:14.5px;color:var(--ink);font-style:normal}
  .slogan{position:absolute;left:230px;top:26px;font-family:'Roboto Slab',serif;font-weight:700;color:var(--teal-deep);line-height:1;text-align:center}
  .slogan .slogan-top{display:block;font-size:43px;letter-spacing:1px}
  .slogan .slogan-bottom{display:block;font-size:30px;margin-top:2px}
  .reminder{position:absolute;left:0;width:292px;top:160px;text-align:center;color:#fff;font-family:'Fira Sans',sans-serif}
  .reminder-lead{font-weight:600;font-size:18.5px;line-height:22.5px}
  .reminder-cta{font-size:13.5px;line-height:15px;margin-top:12px}
  .reminder-phone{font-weight:600;font-size:29px;margin-top:6px;letter-spacing:.5px}
  .reminder-note{font-size:8.5px;line-height:11px;margin-top:6px;font-weight:600}
</style>
</head>
<body>

<section class="card card--front">
  <svg class="layer" width="577" height="440" viewBox="0 0 577 440">
    <defs>
      <linearGradient id="photoTone" x1="0" y1="0" x2="1" y2="1">
        <stop offset="0" stop-color="#9c8a79"/>
        <stop offset=".25" stop-color="#c9bcae"/>
        <stop offset=".5" stop-color="#f1efed"/>
        <stop offset=".72" stop-color="#e8cbb7"/>
        <stop offset="1" stop-color="#dcd8d5"/>
      </linearGradient>
      <linearGradient id="feetTone" x1="0" y1="0" x2="0" y2="1">
        <stop offset="0" stop-color="#f5f3f3"/>
        <stop offset=".3" stop-color="#e7b4a2"/>
        <stop offset=".75" stop-color="#e2b7a6"/>
        <stop offset="1" stop-color="#d8b3a5"/>
      </linearGradient>
    </defs>
    <path d="M0 0 H341 C385 95 378 230 250 295 C180 330 70 330 0 272 Z" fill="url(#photoTone)" role="img" aria-label="Photo of a gloved clinician caring for a patient's toenails"/>
    <path d="M338 -2 C362 45 374 95 373 145" fill="none" stroke="var(--orange)" stroke-width="5"/>
    <path d="M0 272 C70 330 180 330 250 295 C180 342 60 336 0 296 Z" fill="var(--teal)"/>
    <circle cx="440" cy="219" r="105" fill="url(#feetTone)" role="img" aria-label="Photo of a pair of bare feet showing the toenails"/>
    <path d="M379 440 C410 418 440 404 480 402 C520 400 550 404 577 412 V440 Z" fill="var(--teal)"/>
    <path d="M480 400 C520 398 552 402 577 410" fill="none" stroke="var(--orange)" stroke-width="3"/>
  </svg>
  <span class="brand-mark brand-mark--front"></span>
  <div class="brand brand--front">RIDGEVIEW<br>FOOT &amp; ANKLE<span class="brand-site">STEADYSTEPCARE.COM</span></div>
  <p class="tagline">We Keep You Moving</p>
  <h1 class="headline"><span class="hl-orange">Have your nails</span><span class="hl-teal">been taken care of?</span></h1>
  <p class="front-phone">877-555-0142</p>
  <p class="front-site">WWW.STEADYSTEPCARE.COM</p>
  <span class="social-dot social-dot--one"></span>
  <span class="social-dot social-dot--two"></span>
</section>

<section class="card card--back">
  <svg class="layer" width="577" height="440" viewBox="0 0 577 440">
    <rect x="0" y="0" width="450" height="137" fill="var(--paper)"/>
    <rect x="0" y="0" width="292" height="200" fill="var(--paper)"/>
    <path d="M0 170 L150 122 C185 108 215 102 240 108 C262 113 280 124 292 137 V368 H70 V440 H0 Z" fill="var(--orange)"/>
  </svg>
  <span class="brand-mark brand-mark--back"></span>
  <div class="brand brand--back">RIDGEVIEW<br>FOOT &amp; ANKLE<span class="brand-site">STEADYSTEPCARE.COM</span></div>
  <address class="return-address">58 Linden Park Rd.<br>Ste. 210<br>Ashbury, MD 21990</address>
  <h2 class="slogan"><span class="slogan-top">WE KEEP</span><span class="slogan-bottom">YOU MOVING</span></h2>
  <div class="reminder">
    <p class="reminder-lead">We are pleased to<br>inform you may be due for<br>your bimonthly nail care!</p>
    <p class="reminder-cta">Please call our office to<br>schedule your appointment.</p>
    <p class="reminder-phone">(877)555-0142</p>
    <p class="reminder-note">*if you have received nail card within the past<br>two months, please disregard*</p>
  </div>
</section>

</body>
</html>
```